Flyer Design

we are cleaning company specialize in home cleaning, based in North Shore in Auckland (NZ).
Company name RW is initial of bright wren.
we provide professional, high standard,attention to detail service,
to make dust-free, sparkling house and no-stress family.

(business practice)--don't write this title
"colour coded cleaning system"
---we use different colour's microfiber cloths and mop heads for more hygene.
"green and clean"
---we use eco-friendly, non-toxic cleaning products for environment and your family's health.

service we offer
regular cleaning service
--weekly, fortnightly, monthly
one-off cleaning service
---move in/out cleaning
---rental inspection cleaning
---spring cleaning
---open home cleaning
---remodeling clean-up
---special occasion cleaning(event,party)

special cleaning
---window cleaning
---oven cleaning
---house washing(water blasting)

Free in home no obligation consultation and 50% off first service.
contact no; Rob and Helen 021 0487 5620,09-561-2047
e-mail info@rwcleaning.example.nz
www.rwcleaning.example.nz

we would like to see designs that use colours blue and lite pink, clean, bright and friendly image.

Target Market(s)

Woman aged between late 30th to 60th, housewives, career woman, senior etc.

Industry/Entity Type

Environment

Requirements
Should not have
• For the introduction instead of writing what I have written above verbatim, would you be able to go to our website and paraphrase/reword the introduction that's already there?

Also please don't use the picture on the website, we are planning to change the picture. Thanks.

```html
<!DOCTYPE html>
<html lang="en">
<head>
<meta charset="utf-8">
<title>RW Home Cleaning Flyer</title>
<link rel="stylesheet" href="https://fonts.googleapis.com/css2?family=Roboto+Condensed:wght@400;700&family=Open+Sans:wght@300;400;600;700&display=swap">
<style>
  :root {
    --blue: #1c74bf;
    --blue-dark: #1563a8;
    --white: #ffffff;
    --grey-text: #5a5a5a;
    --grey-dark: #4a4a4a;
    --grey-rule: #d4d4d4;
    --stage: #3a3430;
  }
  * { margin: 0; padding: 0; box-sizing: border-box; }
  html, body { width: 1200px; height: 852px; overflow: hidden; }
  body { background: var(--stage); position: relative; font-family: 'Open Sans', sans-serif; }

  .flyer { position: absolute; overflow: hidden; }
  .flyer-back { left: 59px; top: 75px; width: 519px; height: 725px; background: var(--blue); color: var(--white); }
  .flyer-front { left: 594px; top: 73px; width: 518px; height: 727px; background: var(--white); }

  .abs { position: absolute; }

  /* Back */
  .offer-headline { left: 36px; top: 24px; font-family: 'Roboto Condensed', sans-serif; font-weight: 700; font-size: 25px; line-height: 36px; white-space: nowrap; }
  .offer-headline .big { font-size: 31px; }
  .areas-title { right: 36px; top: 106px; font-size: 11px; font-weight: 300; white-space: nowrap; }
  .areas-list { left: 179px; width: 306px; top: 127px; font-size: 6.6px; line-height: 12px; z-index: 2; }

  .photo-grid {
    left: 0; top: 135px; width: 519px; height: 340px; background: var(--white);
    clip-path: path('M0 0 H150 C168 0 166 28 186 28 H519 V338 H402 C380 338 378 318 356 318 H0 Z');
  }
  .photo-grid .photo { position: absolute; }
  .photo-bedroom { left: 1px; top: 2px; width: 270px; height: 179px; background: linear-gradient(135deg, #3d3a36, #7b6f60 60%, #d9c985); }
  .photo-wipe { left: 277px; top: 2px; width: 242px; height: 179px; background: linear-gradient(160deg, #e6e6e4, #cfcfcc 60%, #e8d84a); }
  .photo-bath { left: 1px; top: 186px; width: 270px; height: 154px; background: linear-gradient(135deg, #d8d6d2, #8a8680 55%, #2f2f2f); }
  .photo-window { left: 277px; top: 186px; width: 242px; height: 154px; background: linear-gradient(135deg, #dfe9f0, #b9c9d4 55%, #d6a54a); }

  .contact-title { left: 40px; width: 200px; top: 478px; text-align: center; font-size: 18px; font-weight: 300; }
  .owners-photo { left: 86px; top: 508px; width: 104px; height: 112px; border: 3px solid var(--white); background: linear-gradient(180deg, #d9dfe6, #4f86c6 70%, #2c5f9e); }
  .owners-name { left: 40px; width: 200px; top: 624px; text-align: center; font-size: 11px; font-weight: 700; }
  .contact-email { left: 20px; width: 240px; top: 649px; text-align: center; font-size: 12px; white-space: nowrap; }
  .contact-web { left: 20px; width: 240px; top: 665px; text-align: center; font-size: 13px; font-weight: 700; letter-spacing: 0.5px; white-space: nowrap; }
  .contact-phones { left: 10px; width: 260px; top: 689px; text-align: center; font-family: 'Roboto Condensed', sans-serif; font-weight: 700; font-size: 18px; white-space: nowrap; }

  .section-tab { background: var(--white); color: var(--blue-dark); font-family: 'Roboto Condensed', sans-serif; font-size: 15px; padding: 1px 10px 1px 8px; border-radius: 0 3px 3px 0; white-space: nowrap; }
  .services-tab { left: 286px; top: 494px; }
  .special-tab { left: 286px; top: 647px; }
  .service-group { left: 294px; font-size: 8px; font-weight: 700; white-space: nowrap; }
  .service-list { left: 294px; list-style: none; font-size: 7.6px; line-height: 11.8px; white-space: nowrap; }
  .service-list li { display: flex; align-items: center; gap: 4px; }
  .service-list.inline { display: flex; gap: 8px; }
  .special-list { font-weight: 700; font-size: 8.2px; line-height: 12.8px; }
  .tick { width: 8px; height: 8px; flex: none; }

  /* Front */
  .brand-title { left: 32px; top: 32px; font-family: 'Roboto Condensed', sans-serif; font-weight: 700; font-size: 34px; line-height: 42px; color: var(--blue); white-space: nowrap; }
  .brand-sub { left: 32px; top: 92px; font-size: 25px; font-weight: 400; color: var(--grey-text); line-height: 31px; white-space: nowrap; }
  .hero-photo {
    left: 0; top: 0; width: 518px; height: 500px;
    background: linear-gradient(120deg, #3a2e26 0%, #6b5a4b 35%, #e8e4e0 55%, #bfe23a 75%, #2c2520 100%);
    clip-path: path('M0 165 H300 C322 165 322 136 346 136 H518 V454 H250 C226 454 224 482 200 482 H0 Z');
  }
  .hero-lines { left: 0; top: 0; }
  .practice-tab { left: 0; top: 539px; height: 25px; width: 188px; background: var(--blue); color: var(--white); font-family: 'Roboto Condensed', sans-serif; font-size: 16px; line-height: 25px; padding-left: 25px; clip-path: polygon(0 0, 176px 0, 188px 50%, 176px 100%, 0 100%); white-space: nowrap; }
  .practice-title { left: 25px; font-size: 10.5px; font-weight: 700; color: var(--blue); white-space: nowrap; }
  .practice-text { left: 25px; width: 172px; font-size: 7.6px; line-height: 11.5px; color: var(--grey-text); }
  .front-statement { left: 238px; width: 260px; top: 489px; text-align: center; font-family: 'Roboto Condensed', sans-serif; font-weight: 700; font-size: 16px; line-height: 22px; color: var(--grey-dark); }
  .front-paragraph { left: 234px; width: 262px; top: 608px; font-size: 7.3px; line-height: 14.5px; color: var(--grey-dark); }
  .front-rule { left: 0; top: 680px; width: 518px; height: 2px; background: var(--grey-rule); }
  .footer-band { left: 0; top: 684px; width: 518px; height: 43px; background: var(--blue); color: var(--white); font-size: 17.5px; font-weight: 300; line-height: 43px; padding-left: 32px; white-space: nowrap; letter-spacing: -0.1px; }
</style>
</head>
<body>

<section class="flyer flyer-back">
  <h2 class="abs offer-headline">Free in home no obligation<br>consultation and <span class="big">50% OFF</span> first service</h2>
  <p class="abs areas-title">Areas RW provides service:</p>

  <div class="abs photo-grid">
    <div class="photo photo-bedroom" role="img" aria-label="Tidy modern bedroom with sofa and yellow cushions"></div>
    <div class="photo photo-wipe" role="img" aria-label="Gloved hand wiping tiles with a yellow cloth"></div>
    <div class="photo photo-bath" role="img" aria-label="Clean bathroom with bath and double vanity"></div>
    <div class="photo photo-window" role="img" aria-label="Gloved hand cleaning a window"></div>
  </div>

  <p class="abs areas-list">North shore city wide, Albany, Browns Bay, Mairangi Bay, Rosedale, Foresthill, Glenfield, Takapuna, Greenhithe, Birkenhead, Whangaparaoa, Gulf Harbour, Orewa, and Silverdale (Hibiscus coast area wide), Dairy Flat.</p>

  <h3 class="abs contact-title">Contact Us</h3>
  <div class="abs owners-photo" role="img" aria-label="Portrait of the owners, Rob and Helen"></div>
  <p class="abs owners-name">Rob &amp; Helen</p>
  <p class="abs contact-email">Email: info@rwcleaning.example.nz</p>
  <p class="abs contact-web">www.rwcleaning.example.nz</p>
  <p class="abs contact-phones">021 0487 5620,&nbsp; 09-561-2047</p>

  <svg width="0" height="0" style="position:absolute">
    <symbol id="tick" viewBox="0 0 10 10"><circle cx="5" cy="5" r="5" fill="#fff"/><path d="M2.6 5.2 L4.3 6.9 L7.5 3.4" stroke="#1c74bf" stroke-width="1.6" fill="none"/></symbol>
  </svg>

  <h3 class="abs section-tab services-tab">Service We Offer</h3>
  <p class="abs service-group" style="top:519px">Regular Cleaning Service</p>
  <ul class="abs service-list inline" style="top:533px">
    <li><svg class="tick"><use href="#tick"/></svg>Weekly,</li>
    <li><svg class="tick"><use href="#tick"/></svg>Fortnightly,</li>
    <li><svg class="tick"><use href="#tick"/></svg>Monthly</li>
  </ul>
  <p class="abs service-group" style="top:551px">One-off Cleaning Service</p>
  <ul class="abs service-list" style="top:565px">
    <li><svg class="tick"><use href="#tick"/></svg>Move in/out cleaning</li>
    <li><svg class="tick"><use href="#tick"/></svg>Rental inspection cleaning</li>
    <li><svg class="tick"><use href="#tick"/></svg>Spring cleaning</li>
    <li><svg class="tick"><use href="#tick"/></svg>Open home cleaning</li>
    <li><svg class="tick"><use href="#tick"/></svg>Remodeling clean-up</li>
    <li><svg class="tick"><use href="#tick"/></svg>Special occasion cleaning (event, party)</li>
  </ul>

  <h3 class="abs section-tab special-tab">Special Cleaning</h3>
  <ul class="abs service-list special-list" style="top:671px">
    <li><svg class="tick"><use href="#tick"/></svg>Window Cleaning</li>
    <li><svg class="tick"><use href="#tick"/></svg>Oven Cleaning</li>
    <li><svg class="tick"><use href="#tick"/></svg>House Washing (Water blasting)</li>
  </ul>
</section>

<section class="flyer flyer-front">
  <h1 class="abs brand-title">RW IS INITIAL OF BRIGHT WREN</h1>
  <p class="abs brand-sub">The Lee's Special<br>Home Cleaning Services</p>

  <div class="abs hero-photo" role="img" aria-label="Cleaner in apron and green gloves wiping a kitchen bench"></div>
  <svg class="abs hero-lines" width="518" height="500" viewBox="0 0 518 500">
    <path d="M300 161 C322 161 322 132 346 132 H518" fill="none" stroke="#1c74bf" stroke-width="5"/>
    <path d="M0 486 H200 C224 486 226 458 250 458 H518" fill="none" stroke="#1c74bf" stroke-width="5"/>
  </svg>

  <p class="abs front-statement">We provide professional, high standard, attention to detail service, to make dust-free, sparkling house and no-stress family.</p>

  <h3 class="abs practice-tab">Business Practice</h3>
  <p class="abs practice-title" style="top:575px">Colour Coded Cleaning System</p>
  <p class="abs practice-text" style="top:592px">We use different colour's microfiber cloths and mop heads for more hygene.</p>
  <p class="abs practice-title" style="top:626px">Green And Clean</p>
  <p class="abs practice-text" style="top:643px">We use eco-friendly, non-toxic cleaning for environment and your family's health.</p>

  <p class="abs front-paragraph">We strive to provide a professional, high quality home cleaning services at an affordable price. We do our best to meet every customers requirement whatever your personal cleaning needs are. Because we always aim to make your home sparkle clean and healthy place to live. We love the job!</p>

  <div class="abs front-rule"></div>
  <p class="abs footer-band">Husband and wife team.&nbsp; Dependable, friendly and honest</p>
</section>

</body>
</html>
```